BWLK (a church) flyer for our locality to advertise us

A double-sided colour A5 flyer that introduces our church to our local community. It should include our logo, and be sympathetic to its colours. It should say who we are, when we meet and talk about what we do. It needs to show our location and how to get to us, where you can park, and how to contact us.
We want it to look modern, bright and inviting. More information can be found at www.bwlk-example.org and www.lanternnook-example.org and Facebook lantern.nook.uk

A copy of our previous flyer is attached. Our folks thought it was too dull and emphasised the cafe too much.

Target Market(s)

People within our locality in SE London who may be interested in attending our church, or visiting our cafe, Lantern Nook

Industry/Entity Type

Charity

Font styles to use
Sans Serif

Colors
6b449b
876aae
33a6d7
0455a3
fee18a
ffffff

Requirements
Must have
• A description of who we are at BWLK; what we do; what our values are; when & where we meet & how to contact us. Something to draw people in - a magnetic effect. A modern look & feel. A primary emphasis on our church.
Nice to have
• Design that is sympathetic to our logo colours (livery)
Should not have
• Too much emphasis on the Lantern Nook cafe.

```html
<!DOCTYPE html>
<html lang="en">
<head>
<meta charset="utf-8">
<title>BWLK flyer</title>
<link rel="stylesheet" href="https://fonts.googleapis.com/css2?family=Source+Sans+3:wght@400;600;700&family=Roboto:wght@400;500;700&display=swap">
<style>
:root{
  --stage:#17598a;
  --navy:#262f6e;
  --heading:#2b3a86;
  --ink:#111111;
  --sky-top:#3a9bd0;
  --sky-mid:#a9d3ec;
  --white:#ffffff;
  --peach:#fff0dc;
  --orange:#f7a933;
  --orange-text:#f3a532;
  --rule:#c9b59a;
  --map-grey:#7f7f80;
}
*{box-sizing:border-box;margin:0;padding:0}
html,body{width:1200px;height:1200px;overflow:hidden}
body{background:var(--stage);font-family:"Source Sans 3",sans-serif;color:var(--ink)}
.flyer{position:absolute;left:191px;top:20px;width:818px;height:1160px;overflow:hidden;background:var(--white)}
.sky{position:absolute;left:0;top:0;width:818px;height:454px;background:linear-gradient(180deg,var(--sky-top) 0%,var(--sky-mid) 30%,#eaf5fb 62%,var(--white) 100%)}
.warm{position:absolute;left:0;top:454px;width:818px;height:616px;background:linear-gradient(180deg,var(--peach) 0%,#fde2b8 45%,#fbc572 80%,var(--orange) 100%)}
.footer{position:absolute;left:0;top:1070px;width:818px;height:90px;padding:0 24px;background:var(--navy);color:var(--white);font-size:18.5px;white-space:nowrap;display:flex;align-items:center;justify-content:center;gap:16px}
.footer span{flex:none}
.abs{position:absolute}
.brand{left:54px;top:83px;width:174px;height:146px;background:rgba(255,255,255,.85);display:flex;align-items:center;justify-content:center;gap:10px}
.brand-dot{width:26px;height:26px;border-radius:50%;background:var(--orange)}
.brand-name{font-size:40px;font-weight:600;color:var(--heading)}
h2{font-family:"Source Sans 3",sans-serif;font-weight:700;color:var(--heading);font-size:30px;line-height:1}
.what{left:262px;top:84px;width:520px}
.what p{font-size:19.5px;line-height:29px;margin-top:12px;width:500px}
.overseas{left:45px;top:275px;width:520px}
.overseas .lead{font-size:26px;line-height:34px;margin-top:2px}
.overseas p.small{font-size:17px;line-height:27px;margin-top:10px;padding-left:2px;width:490px}
.kids{left:577px;top:277px;width:187px;height:151px;border:3px solid var(--white);box-shadow:0 2px 4px rgba(0,0,0,.3);background:linear-gradient(135deg,#5b4a6e,#c09a7d 55%,#3c4f8a)}
.room1{left:46px;top:471px;width:243px;height:152px;background:linear-gradient(135deg,#8c6e5c,#d8d0c6 50%,#5a3b34)}
.room2{left:293px;top:471px;width:231px;height:152px;background:linear-gradient(135deg,#c9c3b6,#7a5145 60%,#3b3a36)}
.find{left:573px;top:477px}
.find h2{color:var(--orange-text);font-size:28px}
.find address{font-style:normal;font-family:"Roboto",sans-serif;font-weight:500;font-size:22px;line-height:26.5px;margin-top:10px}
.rule{left:45px;top:650px;width:730px;height:2px;background:var(--rule)}
.map-shadow{left:78px;top:1000px;width:330px;height:22px;background:#111;transform:skewY(-2deg)}
.map-frame{left:43px;top:674px;width:366px;height:349px;background:var(--white);border-radius:10px;padding:10px}
.map{width:100%;height:100%;background:var(--map-grey);display:flex;flex-direction:column;align-items:center;justify-content:center;font-family:"Roboto",sans-serif;color:#1c1c1c}
.map strong{font-size:38px;font-weight:700;line-height:1}
.map span{font-size:21px;margin-top:2px}
.travel{left:446px;top:672px;width:360px;font-family:"Roboto",sans-serif}
.travel h3{font-size:30px;font-weight:700;line-height:1.05;margin-top:12px}
.travel h3:first-child{margin-top:0}
.travel p{font-size:21px;line-height:26px}
.cafe{left:429px;top:952px;width:389px;height:118px;background:radial-gradient(ellipse at 60% 70%,#f6e7cf 0%,#d6a86b 45%,rgba(247,169,51,0) 75%)}
</style>
</head>
<body>
<main class="flyer">
  <div class="sky"></div>
  <div class="warm"></div>

  <div class="abs brand"><span class="brand-dot"></span><span class="brand-name">BWLK</span></div>

  <section class="abs what">
    <h2>WHAT WE DO</h2>
    <p>Our motto is "A place to be loved".<br>We believe that the kingdom of God is best demonstrated in changed lives leading to changed relationships in our homes, work places, schools, work and public places.</p>
  </section>

  <section class="abs overseas">
    <h2>OVERSEAS WE SUPPORT</h2>
    <p class="lead">an orphanage for tribal children in Asia;</p>
    <p class="small">contribute towards a school for orphans and poor children in Jamaica; and make some smaller donations to other projects where we have existing relationships.</p>
  </section>

  <div class="abs kids" role="img" aria-label="Photo of children at the supported orphanage"></div>
  <div class="abs room1" role="img" aria-label="Photo of a church gathering around tables"></div>
  <div class="abs room2" role="img" aria-label="Photo of people meeting in the cafe hall"></div>

  <section class="abs find">
    <h2>FIND US</h2>
    <address>Lantern Nook,<br>Unit 4, Hollin Court,<br>Lee Green,<br>SE12 0XX</address>
  </section>

  <div class="abs rule"></div>

  <div class="abs map-shadow"></div>
  <div class="abs map-frame">
    <div class="map" role="img" aria-label="Map showing the location and nearby train stations">
      <strong>TRAINS</strong><span>the map showing</span>
    </div>
  </div>

  <section class="abs travel">
    <h3>BUSES</h3>
    <p>122, 178, 202, 261, 321 -<br>alight by Greenmart Lee Green/<br>Old Lantern Arms</p>
    <h3>TRAINS</h3>
    <p>Lee, Lewisham &amp; Blackheath</p>
    <h3>PARKING</h3>
    <p>FREE parking in car park behind<br>car wash in Elm Bank Rd</p>
  </section>

  <div class="abs cafe" role="img" aria-label="Illustration of a coffee cup and cake for the Lantern Nook cafe"></div>

  <footer class="footer">
    <span>www.bwlk-example.org</span><span>|</span>
    <span>www.lanternnook-example.org.uk</span><span>|</span>
    <span>Facebook lantern.nook.uk</span>
  </footer>
</main>
</body>
</html>
```